REDESIGN MAIN BANNER IMAGE FOR MARKETING WEBSITE

I feel like my main banner image is too busy but I like it but i want to see other options. www.brightlanepromoworks.biz I want a nice professional clean design that goes with current theme of site. Must look professional and show the variety of incentives we offer but not be overwelming.

My business is called Brightlane Promo Works and I provide businesses around the world with marketing incentives that they can use to create exciting promotions and contest and marketing giveaways to help attract more customers.

I provide a variety of different types of incentives such as Vacation Certificates, Dining Vouchers, Hotel Savings Cards, Smart Watches, Etc. that businesses can use in their marketing efforts.

I want my main banner image to reflect the variety of different categories of incentives... that I offer here: https://www.brightlanepromoworks.biz/incentives

We can use images of certificates or images.....I just want the content to be the same:

CONTENT FOR MAIN BANNER IMAGE:
INCREASE LEADS AND SALES OVERNIGHT

CREATE EXCITING MARKETING PROMOTIONS GIVING AWAY SMART DEVICES, VACATION CERTIFICATES, DINING VOUCHERS AND OTHER INCENTIVES TO YOUR CUSTOMERS

GET A FREE SAMPLE PACKAGE FOR A LIMITED TIME ONLY

Target Market(s)

b2b business owners, ceo, president, owner, founder

Industry/Entity Type

Promotional

Requirements
Must have
• Hi guys keep in mind the finished product will have to be 1800x840

Nice to have
• I want a nice professional clean design that goes with current theme of site. Must look professional and show the variety of incentives we offer but not be overwelming.
Should not have

```html
<!DOCTYPE html>
<html lang="en">
<head>
<meta charset="utf-8">
<title>Brightlane Promo Works – Main Banner</title>
<link href="https://fonts.googleapis.com/css2?family=Bebas+Neue&family=Montserrat:wght@400;600;700&display=swap" rel="stylesheet">
<style>
:root{
  --stage:#e4e4e4;
  --blue-deep:#1b3e8c;
  --blue:#1467bd;
  --blue-nav:#1670c4;
  --green:#4cae4f;
  --red:#d41f1f;
  --red-dark:#a81313;
  --label-blue:#1d5aa6;
  --row-gray:#eceef2;
  --white:#ffffff;
  --login-gray:#4a4d52;
}
*{box-sizing:border-box;margin:0;padding:0}
html,body{width:1057px;height:1200px;overflow:hidden;background:var(--stage)}
.canvas{position:relative;width:1057px;height:1200px;background:var(--stage);overflow:hidden}

.banner{position:absolute;width:1057px;height:494px;background:var(--white);overflow:hidden}
.banner--preview{left:114px;top:130px;transform:scale(.7645);transform-origin:0 0;box-shadow:0 22px 22px -12px rgba(0,0,0,.45)}
.banner--live{left:0;top:706px}

.hero{position:absolute;left:0;top:0;width:576px;height:494px;color:var(--white)}
.hero__bg{position:absolute;inset:0}
.hero__title{position:absolute;left:54px;top:48px;font-family:"Bebas Neue",sans-serif;font-weight:400;font-size:88px;line-height:78px;letter-spacing:-.5px;text-shadow:2px 3px 4px rgba(0,0,0,.35)}
.hero__copy{position:absolute;left:54px;top:296px;width:480px;font-family:"Montserrat",sans-serif;font-weight:700;font-size:14.2px;line-height:18.5px;text-transform:uppercase}
.cta{position:absolute;left:44px;top:372px;width:422px;height:67px;background:linear-gradient(90deg,var(--red) 0%,#c81a1a 60%,var(--red-dark) 100%);box-shadow:0 6px 8px rgba(0,0,0,.35);padding:9px 0 0 24px;font-family:"Montserrat",sans-serif;font-size:23.5px;line-height:28px;color:var(--white);white-space:nowrap}
.cta strong{font-weight:700}

.catalog{position:absolute;left:576px;top:0;width:481px;height:494px;background:var(--white)}
.row{position:absolute;left:0;width:481px;background:var(--row-gray)}
.row--1{top:20px;height:142px}
.row--2{top:178px;height:138px}
.row--3{top:332px;height:140px}
.cert{position:absolute;width:108px;height:118px;background:linear-gradient(180deg,#f2f2f2 0%,#b8c3cf 26%,#c62020 30%,#ffffff 36%,#ffffff 78%,#c62020 82%,#f4f4f4 100%);box-shadow:2px 3px 5px rgba(0,0,0,.35)}
.label{position:absolute;height:22px;padding-left:7px;font-family:"Bebas Neue",sans-serif;font-size:17px;line-height:23px;color:var(--white);letter-spacing:.3px;white-space:nowrap;clip-path:polygon(0 0,88% 0,100% 100%,0 100%)}
.label--blue{background:var(--label-blue)}
.label--red{background:var(--red)}

.site-header{position:absolute;left:0;top:646px;width:1057px;height:60px;background:var(--blue-nav)}
.brand{position:absolute;left:0;top:0;width:302px;height:60px;background:var(--white);clip-path:polygon(0 0,280px 0,302px 30px,280px 60px,0 60px);display:flex;align-items:center;padding-left:20px;gap:9px}
.brand__mark{width:16px;height:16px;background:var(--blue-nav)}
.brand__name{font-family:"Montserrat",sans-serif;font-weight:700;font-size:17px;color:var(--blue-nav);white-space:nowrap}
.nav{position:absolute;left:0;top:0;width:734px;height:60px;font-family:"Montserrat",sans-serif;font-weight:600;font-size:10.4px;line-height:14px;color:var(--white)}
.nav__item{position:absolute;top:22px;white-space:nowrap}
.nav__sep{position:absolute;top:20px;width:1px;height:28px;background:rgba(255,255,255,.35)}
.account{position:absolute;top:0;height:60px;width:62px;display:flex;flex-direction:column;align-items:center;justify-content:center;gap:5px;font-family:"Montserrat",sans-serif;font-size:10px;color:var(--white)}
.account--login{left:734px;background:var(--login-gray)}
.account--signup{left:796px;background:var(--blue-nav)}
.contact{position:absolute;left:858px;top:0;width:199px;height:60px;background:var(--green);display:flex;align-items:center;padding-left:8px;gap:10px;font-family:"Montserrat",sans-serif;font-weight:700;font-size:10px;line-height:14px;color:var(--white);white-space:nowrap}
</style>
</head>
<body>
<div class="canvas">

  <section class="banner banner--preview" aria-label="Main banner">
    <div class="hero">
      <svg class="hero__bg" width="576" height="494" viewBox="0 0 576 494">
        <defs>
          <linearGradient id="blueA" x1="0" y1="0" x2="1" y2="1">
            <stop offset="0" stop-color="#1b3d8a"/><stop offset=".6" stop-color="#1563b8"/><stop offset="1" stop-color="#137ac8"/>
          </linearGradient>
          <linearGradient id="greenA" x1="0" y1="0" x2="1" y2="0">
            <stop offset="0" stop-color="#1d7bb2"/><stop offset=".5" stop-color="#359c80"/><stop offset="1" stop-color="#4cae4f"/>
          </linearGradient>
        </defs>
        <rect width="576" height="494" fill="url(#blueA)"/>
        <polygon points="0,370 210,265 250,295 410,150 455,180 576,92 576,494 0,494" fill="url(#greenA)"/>
      </svg>
      <h1 class="hero__title">Increase<br>Leads and Sales<br>Overnight</h1>
      <p class="hero__copy">Create exciting marketing promotions givingaway smart devices, vacation certificates, dining vouchers and other incentives to your customers</p>
      <div class="cta"><strong>Get A Free Sample</strong> Package<br>For A Limited Time Only</div>
    </div>
    <div class="catalog">
      <div class="row row--1"></div><div class="row row--2"></div><div class="row row--3"></div>
      <div class="cert" style="left:40px;top:24px" role="img" aria-label="Vacation certificate sample"></div>
      <div class="label label--blue" style="left:40px;top:140px;width:130px">Vacation Certs</div>
      <div class="cert" style="left:176px;top:24px" role="img" aria-label="Airfare certificate sample"></div>
      <div class="label label--blue" style="left:176px;top:140px;width:130px">Airfare Certs</div>
      <div class="cert" style="left:312px;top:24px" role="img" aria-label="Cruise certificate sample"></div>
      <div class="label label--blue" style="left:312px;top:140px;width:130px">Cruise Certs</div>
      <div class="cert" style="left:102px;top:178px" role="img" aria-label="Las Vegas certificate sample"></div>
      <div class="label label--red" style="left:102px;top:294px;width:130px">Las Vegas Certs</div>
      <div class="cert" style="left:250px;top:178px" role="img" aria-label="Resort and condo certificate sample"></div>
      <div class="label label--red" style="left:250px;top:294px;width:158px">Resorts &amp; Condo Certs</div>
      <div class="cert" style="left:40px;top:332px" role="img" aria-label="Fitness watch certificate sample"></div>
      <div class="label label--blue" style="left:40px;top:450px;width:148px">Fitness Watch Certs</div>
      <div class="cert" style="left:178px;top:332px" role="img" aria-label="Dining certificate sample"></div>
      <div class="label label--blue" style="left:178px;top:450px;width:134px">Dinning Certs</div>
      <div class="cert" style="left:316px;top:332px" role="img" aria-label="Cruise certificate sample"></div>
      <div class="label label--blue" style="left:316px;top:450px;width:134px">Cruise Certs</div>
    </div>
  </section>

  <header class="site-header">
    <div class="brand"><span class="brand__mark"></span><span class="brand__name">Brightlane Promo Works</span></div>
    <nav class="nav">
      <span class="nav__item" style="left:331px">Home</span>
      <span class="nav__sep" style="left:369px"></span>
      <span class="nav__item" style="left:375px">The<br>Incentives</span>
      <span class="nav__sep" style="left:444px"></span>
      <span class="nav__item" style="left:450px">Samples</span>
      <span class="nav__sep" style="left:501px"></span>
      <span class="nav__item" style="left:507px">Industries</span>
      <span class="nav__sep" style="left:564px"></span>
      <span class="nav__item" style="left:570px">Testimonials</span>
      <span class="nav__sep" style="left:640px"></span>
      <span class="nav__item" style="left:646px">Faq</span>
      <span class="nav__sep" style="left:672px"></span>
      <span class="nav__item" style="left:679px">Contact<br>Us</span>
    </nav>
    <div class="account account--login">
      <svg width="14" height="14" viewBox="0 0 14 14"><circle cx="7" cy="4" r="3.2" fill="#fff"/><path d="M1 14c0-4 2.7-5.6 6-5.6s6 1.6 6 5.6z" fill="#fff"/></svg>
      LOGIN
    </div>
    <div class="account account--signup">
      <svg width="16" height="16" viewBox="0 0 16 16"><circle cx="8" cy="8" r="7" fill="none" stroke="#fff" stroke-width="1.5"/><path d="M8 12V5M5 7.5L8 4.5l3 3" fill="none" stroke="#fff" stroke-width="1.6"/></svg>
      SIGN UP
    </div>
    <div class="contact">
      <svg width="16" height="28" viewBox="0 0 16 28"><rect x="1" y="1" width="14" height="26" rx="2.5" fill="none" stroke="#fff" stroke-width="1.6"/><line x1="1" y1="5" x2="15" y2="5" stroke="#fff" stroke-width="1.2"/><line x1="1" y1="22" x2="15" y2="22" stroke="#fff" stroke-width="1.2"/></svg>
      <div>CALL US: 1-555-204-3187<br>TEXT US: 1-555-204-3190</div>
    </div>
  </header>

  <section class="banner banner--live" aria-label="Main banner">
    <div class="hero">
      <svg class="hero__bg" width="576" height="494" viewBox="0 0 576 494">
        <defs>
          <linearGradient id="blueB" x1="0" y1="0" x2="1" y2="1">
            <stop offset="0" stop-color="#1b3d8a"/><stop offset=".6" stop-color="#1563b8"/><stop offset="1" stop-color="#137ac8"/>
          </linearGradient>
          <linearGradient id="greenB" x1="0" y1="0" x2="1" y2="0">
            <stop offset="0" stop-color="#1d7bb2"/><stop offset=".5" stop-color="#359c80"/><stop offset="1" stop-color="#4cae4f"/>
          </linearGradient>
        </defs>
        <rect width="576" height="494" fill="url(#blueB)"/>
        <polygon points="0,370 210,265 250,295 410,150 455,180 576,92 576,494 0,494" fill="url(#greenB)"/>
      </svg>
      <h1 class="hero__title">Increase<br>Leads and Sales<br>Overnight</h1>
      <p class="hero__copy">Create exciting marketing promotions givingaway smart devices, vacation certificates, dining vouchers and other incentives to your customers</p>
      <div class="cta"><strong>Get A Free Sample</strong> Package<br>For A Limited Time Only</div>
    </div>
    <div class="catalog">
      <div class="row row--1"></div><div class="row row--2"></div><div class="row row--3"></div>
      <div class="cert" style="left:40px;top:24px" role="img" aria-label="Vacation certificate sample"></div>
      <div class="label label--blue" style="left:40px;top:140px;width:130px">Vacation Certs</div>
      <div class="cert" style="left:176px;top:24px" role="img" aria-label="Airfare certificate sample"></div>
      <div class="label label--blue" style="left:176px;top:140px;width:130px">Airfare Certs</div>
      <div class="cert" style="left:312px;top:24px" role="img" aria-label="Cruise certificate sample"></div>
      <div class="label label--blue" style="left:312px;top:140px;width:130px">Cruise Certs</div>
      <div class="cert" style="left:102px;top:178px" role="img" aria-label="Las Vegas certificate sample"></div>
      <div class="label label--red" style="left:102px;top:294px;width:130px">Las Vegas Certs</div>
      <div class="cert" style="left:250px;top:178px" role="img" aria-label="Resort and condo certificate sample"></div>
      <div class="label label--red" style="left:250px;top:294px;width:158px">Resorts &amp; Condo Certs</div>
      <div class="cert" style="left:40px;top:332px" role="img" aria-label="Fitness watch certificate sample"></div>
      <div class="label label--blue" style="left:40px;top:450px;width:148px">Fitness Watch Certs</div>
      <div class="cert" style="left:178px;top:332px" role="img" aria-label="Dining certificate sample"></div>
      <div class="label label--blue" style="left:178px;top:450px;width:134px">Dinning Certs</div>
      <div class="cert" style="left:316px;top:332px" role="img" aria-label="Cruise certificate sample"></div>
      <div class="label label--blue" style="left:316px;top:450px;width:134px">Cruise Certs</div>
    </div>
  </section>

</div>
</body>
</html>
```